Stretch on the Green with Mara

I want to advertise my Stretch on the Green classes for Summer. Classes are outside at the lovely local park. Dunmore field. 82 Halcombe St. Westlow.
Classes are for beginners to advance levels.
Classes start Monday, October 17th.
Monday 6pm Beginners
Tuesday 6pm Intermediate
Thursday 6pm Intermediate/Advance
Saturday 9am All fitness levels
My Pilates classes are specially designed to help improve strength and flexibility but as well will also improve posture, reduce stress and develop control and endurance in the entire body.
Booking essential. Limited numbers so I can make sure the correct technique is always being followed.
For more info or to book contact details:
Mara 027385916
mara@corestudiomara.net
www.corestudiomara.net
$15 Per Session

Target Market(s)

Males and Females ages 35plus.

Industry/Entity Type

Fitness

Font styles to use
Sans Serif

Requirements
Must have
• My logo. Contact details. A Park that looks lovely to exercise at.
Nice to have
• Summer looking. Trees - inspiration to be exercising outside

```html
<!DOCTYPE html>
<html lang="en">
<head>
<meta charset="utf-8">
<title>Stretch on the Green with Mara</title>
<link href="https://fonts.googleapis.com/css2?family=Montserrat:wght@400;500;600;700;800&family=Oswald:wght@500;600&display=swap" rel="stylesheet">
<style>
  :root{
    --stage:#3d3d3d;
    --magenta:#e0127a;
    --magenta-soft:rgba(196,20,110,.78);
    --green:#22c48f;
    --lime:#b6f22c;
    --grey:#e6e6e6;
    --ink:#2b2b2b;
    --white:#ffffff;
    --leaf-dark:#2f5a2a;
    --leaf-mid:#5f8f3c;
    --leaf-light:#a9c77a;
  }
  *{margin:0;padding:0;box-sizing:border-box}
  html,body{width:1200px;height:1177px;overflow:hidden;background:var(--stage)}
  body{font-family:'Montserrat',sans-serif;color:var(--ink)}
  .flyer{position:absolute;left:251px;top:130px;width:718px;height:927px;background:var(--white);overflow:hidden}
  .park-photo{position:absolute;left:0;top:0;width:718px;height:560px;
    background:
      radial-gradient(ellipse at 30% 20%, rgba(230,240,200,.8), transparent 45%),
      radial-gradient(ellipse at 85% 40%, var(--leaf-dark), transparent 55%),
      linear-gradient(180deg,#c9d9b4 0%,var(--leaf-light) 35%,var(--leaf-mid) 65%,#4f7f32 100%)}
  .grey-field{position:absolute;left:0;top:520px;width:718px;height:150px;background:var(--grey)}
  .grey-curve{position:absolute;left:0;top:470px;width:718px;height:80px}
  .headline-band{position:absolute;left:0;top:38px;width:538px;height:111px;background:var(--magenta-soft)}
  .headline-main{position:absolute;left:36px;top:40px;font-weight:800;font-size:98px;line-height:110px;color:var(--white);letter-spacing:1px}
  .headline-sub{position:absolute;right:22px;top:160px;text-align:right;color:var(--white);font-weight:700}
  .headline-sub .small{display:block;font-size:46px;line-height:48px;font-weight:600}
  .headline-sub .big{display:block;font-size:92px;line-height:88px}
  .dots{position:absolute;left:449px;top:292px;width:246px;height:10px}
  .info-card{position:absolute;top:455px;height:117px;border-radius:6px;text-align:center;box-shadow:0 3px 6px rgba(0,0,0,.25)}
  .card-levels{left:29px;width:206px;background:var(--magenta);color:var(--white)}
  .date-tab{position:absolute;left:269px;top:455px;width:199px;height:40px;border-radius:6px 6px 0 0;background:var(--green)}
  .card-date{left:277px;top:462px;height:110px;width:183px;background:var(--white);padding-top:9px}
  .card-venue{left:503px;width:182px;background:var(--green);color:var(--white)}
  .card-tab{position:absolute;left:-8px;top:0;width:16px;height:40px;border-radius:6px 0 0 0}
  .card-levels .card-tab{background:var(--white)}
  .card-venue .card-tab{background:var(--magenta)}
  .card-icon{display:block;margin:10px auto 4px}
  .card-text{font-weight:600;font-size:15.5px;line-height:19px}
  .date-lead{font-weight:600;font-size:14.5px;line-height:16px;color:var(--green)}
  .date-day{font-weight:700;font-size:14.5px;color:var(--magenta)}
  .date-num{font-family:'Oswald',sans-serif;font-weight:600;font-size:52px;line-height:60px;color:var(--magenta);margin-top:2px}
  .date-num sup{font-size:24px;vertical-align:18px}
  .intro{position:absolute;left:50px;top:602px;width:618px;text-align:center;font-weight:500;font-size:15px;line-height:19px}
  .booking-band{position:absolute;left:0;top:670px;width:718px;height:120px;background:var(--white)}
  .booking-green{position:absolute;left:0;top:0;width:300px;height:120px;background:var(--green)}
  .booking-title{position:absolute;left:38px;top:14px;font-family:'Oswald',sans-serif;font-weight:500;font-size:45px;line-height:46px;color:var(--white)}
  .price{position:absolute;left:241px;top:6px;width:108px;height:108px;border-radius:50%;border:5px solid var(--white);
    background:linear-gradient(180deg,var(--green),var(--magenta));color:var(--white);text-align:center;box-shadow:0 0 0 3px var(--magenta)}
  .price-num{font-family:'Oswald',sans-serif;font-weight:600;font-size:38px;line-height:44px;margin-top:10px}
  .price-label{font-size:13px;line-height:14px;font-weight:600}
  .schedule{position:absolute;left:377px;top:20px;list-style:none;font-size:15.5px;line-height:20px;font-weight:500}
  .schedule li{display:flex}
  .schedule .day{width:80px;font-weight:600}
  .schedule .time{width:50px}
  .schedule .arrow{width:13px;font-size:11px;color:var(--magenta)}
  .schedule li:nth-child(even) .day,.schedule li:nth-child(even) .arrow{color:var(--green)}
  .schedule li:nth-child(odd) .day{color:var(--magenta)}
  .notice{position:absolute;left:0;top:790px;width:718px;height:30px;background:var(--magenta);color:var(--white);text-align:center;font-weight:600;font-size:15px;line-height:30px}
  .footer-brand{position:absolute;left:0;top:820px;width:295px;height:107px;background:var(--white);text-align:center}
  .brand-mark{display:block;width:26px;height:26px;border-radius:50%;background:#7a7a7a;margin:20px auto 12px}
  .brand-name{font-size:21px;font-weight:500;color:var(--magenta);letter-spacing:1px}
  .footer-contact{position:absolute;left:295px;top:820px;width:423px;height:107px;background:var(--grey);padding:16px 0 0 28px}
  .contact-title{font-weight:500;font-size:14.5px;margin-left:18px;margin-bottom:4px}
  .contact-line{display:flex;align-items:center;gap:6px;font-size:14px;line-height:19px;font-weight:500}
  .contact-line .who{color:var(--magenta)}
  .contact-web{font-weight:700;font-size:17px;color:var(--magenta)}
</style>
</head>
<body>
<main class="flyer">
  <div class="park-photo" role="img" aria-label="Photo of a woman doing a plank on an exercise ball on the grass in a sunny, tree-lined park"></div>
  <svg class="grey-curve" viewBox="0 0 718 80" preserveAspectRatio="none"><path d="M0 80 Q359 20 718 80 Z" fill="#e6e6e6"/></svg>
  <div class="grey-field"></div>

  <div class="headline-band"></div>
  <h1 class="headline-main">STRETCH</h1>
  <div class="headline-sub"><span class="small">on the</span><span class="big">green</span></div>
  <svg class="dots" viewBox="0 0 246 10"><line x1="5" y1="5" x2="243" y2="5" stroke="#b6f22c" stroke-width="6" stroke-linecap="round" stroke-dasharray="0 10.5"/></svg>

  <section class="info-card card-levels">
    <span class="card-tab"></span>
    <svg class="card-icon" width="42" height="42" viewBox="0 0 42 42"><circle cx="21" cy="21" r="18" fill="none" stroke="#fff" stroke-width="3"/><path d="M12 21l7 7 14-16" fill="none" stroke="#fff" stroke-width="4" stroke-linecap="round" stroke-linejoin="round"/></svg>
    <p class="card-text">Classes are for<br>BEGINNERS to<br>ADVANCE levels</p>
  </section>

  <div class="date-tab"></div>
  <section class="info-card card-date">
    <p class="date-lead">Classes start<br><span class="date-day">MONDAY</span></p>
    <p class="date-num">17<sup>TH</sup>OCT</p>
  </section>

  <section class="info-card card-venue">
    <span class="card-tab"></span>
    <svg class="card-icon" width="26" height="36" viewBox="0 0 26 36"><path d="M13 1C6 1 1 6 1 13c0 9 12 22 12 22s12-13 12-22C25 6 20 1 13 1z" fill="#fff"/><circle cx="13" cy="13" r="5" fill="#22c48f"/></svg>
    <p class="card-text">DUNMORE FIELD<br>82 Halcombe St.<br>Westlow.</p>
  </section>

  <p class="intro">My Pilates classes are specially designed to help improve strength and flexibility but as well will also improve posture, reduce stress and develop control and endurance in the entire body.</p>

  <section class="booking-band">
    <div class="booking-green"></div>
    <h2 class="booking-title">BOOKING<br>ESSENTIAL</h2>
    <div class="price"><p class="price-num">15$</p><p class="price-label">per<br>session</p></div>
    <ul class="schedule">
      <li><span class="arrow">▶</span><span class="day">Monday</span><span class="time">6pm</span><span>Beginners</span></li>
      <li><span class="arrow">▶</span><span class="day">Tuesday</span><span class="time">6pm</span><span>Intermediate</span></li>
      <li><span class="arrow">▶</span><span class="day">Thursday</span><span class="time">6pm</span><span>Intermediate/Advance</span></li>
      <li><span class="arrow">▶</span><span class="day">Saturday</span><span class="time">9am</span><span>All fitness levels</span></li>
    </ul>
  </section>

  <p class="notice">Limited numbers so I can make sure the correct technique is always being followed.</p>

  <footer class="footer-brand">
    <span class="brand-mark"></span>
    <p class="brand-name">CORE STUDIO MARA</p>
  </footer>
  <footer class="footer-contact">
    <p class="contact-title">FOR MORE INFO OR TO BOOK CONTACT DETAILS:</p>
    <p class="contact-line"><svg width="12" height="12" viewBox="0 0 12 12"><path d="M2 1l2 0 1 3-1.5 1a7 7 0 0 0 3.5 3.5L8 7l3 1v2a1 1 0 0 1-1 1A9 9 0 0 1 1 2a1 1 0 0 1 1-1z" fill="#e0127a"/></svg><span class="who">Mara</span> 027385916</p>
    <p class="contact-line"><svg width="12" height="10" viewBox="0 0 12 10"><rect x="0" y="0" width="12" height="10" rx="1" fill="#e0127a"/><path d="M0 1l6 5 6-5" fill="none" stroke="#fff" stroke-width="1.2"/></svg>mara@corestudiomara.net</p>
    <p class="contact-line contact-web"><svg width="13" height="13" viewBox="0 0 14 14"><circle cx="7" cy="7" r="6" fill="none" stroke="#e0127a" stroke-width="1.6"/><ellipse cx="7" cy="7" rx="2.5" ry="6" fill="none" stroke="#e0127a" stroke-width="1.2"/><line x1="1" y1="7" x2="13" y2="7" stroke="#e0127a" stroke-width="1.2"/></svg>www.corestudiomara.net</p>
  </footer>
</main>
</body>
</html>
```